Blue Heron IT Business Card - Clean, Simple

Need a simple, clean standard sized business card for an IT consulting business using existing logo and company colours. Background should be mainly white. Feel free to be creative but clean, simple, quiet design is preferred. Font is specified in logo but any sans serif fonts work.

Contact Information for card is as follows (doesn't need to be in this exact order):

Malcolm Pettigrew
Owner
malcolm@blueheronit.ca
705-412-9083
www.blueheronit.ca

Target Market(s)

Small to medium sized business.

Industry/Entity Type

IT Consulting

Contact Information for Business Card

Logo and contact info.

Font styles to use
Sans Serif

Colors
EE7325
F08F49
F5BC92
FAE3D3
FDF4ED

Requirements
Must have
• All white or mostly white background.

```html
<!DOCTYPE html>
<html lang="en">
<head>
<meta charset="utf-8">
<title>Blue Heron IT – Business Card</title>
<link rel="stylesheet" href="https://fonts.googleapis.com/css2?family=Lato:wght@400;700&family=Montserrat:wght@500;700&display=swap">
<style>
  :root {
    --orange: #ee7325;
    --orange-soft: #f08f49;
    --peach: #f5bc92;
    --blush: #fae3d3;
    --cream: #fdf4ed;
    --ink: #1f1f1f;
    --grey-text: #4a4a4a;
    --rule: #9a9a9a;
    --ghost: #eef0f3;
    --paper: #ffffff;
    --stage: #e4e5e7;
  }
  * { box-sizing: border-box; margin: 0; padding: 0; }
  html, body { width: 1200px; height: 952px; overflow: hidden; }
  body {
    background: var(--stage);
    font-family: "Lato", Arial, sans-serif;
    position: relative;
  }
  .card {
    position: absolute;
    width: 525px;
    height: 300px;
    background: var(--paper);
    box-shadow: 0 6px 18px rgba(0,0,0,.18);
    overflow: hidden;
  }
  .card--front { left: 50px; top: 326px; }
  .card--back  { left: 625px; top: 326px; }

  /* Front */
  .holder { position: absolute; left: 30px; top: 30px; }
  .holder__name {
    font-family: "Montserrat", Arial, sans-serif;
    font-weight: 700;
    font-size: 20px;
    letter-spacing: .2px;
    color: var(--orange);
    text-transform: uppercase;
  }
  .holder__role {
    display: flex; align-items: center; gap: 8px;
    margin-top: 2px;
    font-size: 14px;
    color: var(--grey-text);
  }
  .holder__rule { width: 200px; height: 1px; background: var(--rule); }

  .decor-mark {
    position: absolute;
    left: 36px; top: 96px;
    width: 170px; height: 170px;
    border-radius: 50%;
    background: var(--ghost);
  }

  .band {
    position: absolute;
    left: 0; bottom: 28px;
    width: 300px; height: 62px;
    background: var(--orange);
    display: flex; align-items: center;
    padding-left: 26px;
  }
  .band__name {
    font-family: "Montserrat", Arial, sans-serif;
    font-weight: 700;
    font-size: 30px;
    color: var(--paper);
    white-space: nowrap;
  }

  .contact {
    position: absolute;
    right: 30px; top: 150px;
    list-style: none;
    display: flex; flex-direction: column; gap: 9px;
    align-items: flex-end;
  }
  .contact__item {
    display: flex; align-items: center; gap: 9px;
    font-size: 13px;
    color: var(--grey-text);
  }
  .contact__icon {
    width: 18px; height: 18px;
    border-radius: 4px;
    background: var(--ink);
    display: flex; align-items: center; justify-content: center;
  }

  /* Back */
  .brand {
    position: absolute; inset: 0;
    display: flex; align-items: center; justify-content: center; gap: 14px;
  }
  .brand__dot {
    width: 34px; height: 34px; border-radius: 50%;
    background: var(--orange);
  }
  .brand__name {
    font-family: "Montserrat", Arial, sans-serif;
    font-weight: 700;
    font-size: 40px;
    color: var(--ink);
  }
</style>
</head>
<body>

  <article class="card card--front">
    <div class="decor-mark" role="img" aria-label="Faint brand emblem watermark"></div>

    <header class="holder">
      <h1 class="holder__name">Malcolm Pettigrew</h1>
      <p class="holder__role">Owner <span class="holder__rule"></span></p>
    </header>

    <ul class="contact">
      <li class="contact__item">705-412-9083
        <span class="contact__icon">
          <svg width="11" height="11" viewBox="0 0 24 24"><path fill="#fff" d="M6.6 10.8a15 15 0 0 0 6.6 6.6l2.2-2.2c.3-.3.7-.4 1-.2 1.1.4 2.3.6 3.6.6.6 0 1 .4 1 1V20c0 .6-.4 1-1 1A17 17 0 0 1 3 4c0-.6.4-1 1-1h3.5c.6 0 1 .4 1 1 0 1.3.2 2.5.6 3.6.1.3 0 .7-.2 1z"/></svg>
        </span>
      </li>
      <li class="contact__item">malcolm@blueheronit.ca
        <span class="contact__icon">
          <svg width="11" height="11" viewBox="0 0 24 24"><rect x="3" y="5" width="18" height="14" rx="1" fill="none" stroke="#fff" stroke-width="2"/><path d="M3 6l9 7 9-7" fill="none" stroke="#fff" stroke-width="2"/></svg>
        </span>
      </li>
      <li class="contact__item">www.blueheronit.ca
        <span class="contact__icon">
          <svg width="11" height="11" viewBox="0 0 24 24"><path fill="#fff" d="M12 2a7 7 0 0 0-7 7c0 5 7 13 7 13s7-8 7-13a7 7 0 0 0-7-7zm0 9.5A2.5 2.5 0 1 1 12 6.5a2.5 2.5 0 0 1 0 5z"/></svg>
        </span>
      </li>
    </ul>

    <div class="band"><span class="band__name">Blue Heron IT</span></div>
  </article>

  <article class="card card--back">
    <div class="brand">
      <span class="brand__dot"></span>
      <span class="brand__name">Blue Heron IT</span>
    </div>
  </article>

</body>
</html>
```